Presentation Folder - Stagger Cut Fliers
Keystone Realty Group
Presentation Folder - Stagger Cut Fliers - Real Estate
Creative Brief
Real Estate
Corporate. Our target audience are real estate agents and brokers. This is an industry where image and perception matter, so these designs need to invoke professionalism, be creative, and invoke confidence in our services.
The presentation folder itself needs to be very simple, but again, very professional and aesthetically pleasing. At a minimum, we need our logo on the font and the company contact information on the back. The stagger cut fliers themselves need to have the ability to put information on the front and back of the flier. There are five pages for the fliers, so you can either design five unique pages or have a template that can work for all of them. You can use filler text like that in the attached document. The fliers aren't just going to be text. You can add filler images to make more appealing, such as on the consumer demand page you can leave a spot where we can put the image of a billboard.

```html
<!DOCTYPE html>
<html lang="en">
<head>
<meta charset="utf-8">
<title>Keystone Realty Group – Presentation Folder and Stagger Cut Fliers</title>
<link href="https://fonts.googleapis.com/css2?family=Open+Sans:wght@400;600;700&display=swap" rel="stylesheet">
<style>
  :root {
    --blue: #1f7cc4;
    --blue-dark: #0f5a99;
    --blue-light: #4ba6e3;
    --sky: #cfe6f7;
    --paper: #ffffff;
    --paper-shade: #eef2f6;
    --ink: #5b6670;
    --line: #e3e8ee;
    --stage: #ffffff;
  }
  * { box-sizing: border-box; margin: 0; padding: 0; }
  html, body { width: 1200px; height: 346px; overflow: hidden; background: var(--stage); }
  body { position: relative; font-family: "Open Sans", Arial, sans-serif; color: var(--ink); }

  .flier {
    position: absolute; top: 17px; width: 155px; height: 319px;
    background: var(--paper); border: 1px solid var(--line);
    box-shadow: 0 1px 3px rgba(0,0,0,.18); overflow: hidden;
  }
  .flier-title {
    position: absolute; left: 10px; top: 12px;
    font-size: 5.5px; font-weight: 700; letter-spacing: .4px;
    text-transform: uppercase; color: var(--blue); white-space: nowrap;
  }
  .flier-wave { position: absolute; left: 0; top: 22px; width: 155px; height: 46px; }
  .photo { position: absolute; left: 0; top: 58px; width: 155px; height: 118px; }
  .photo-house { background: linear-gradient(180deg, #8fc3ea 0%, #c9dde8 45%, #7d8f6a 78%, #4f6a3c 100%); }
  .photo-home { background: linear-gradient(180deg, #b7d7ef 0%, #e4e9e6 50%, #8aa36a 80%, #5b7a40 100%); }
  .photo-hands { background: linear-gradient(180deg, #ffffff 0%, #e8ecef 40%, #c2b6a6 70%, #3c4650 100%); }
  .photo-street { background: linear-gradient(180deg, #9fcdf0 0%, #dfe6ea 45%, #9aa89a 75%, #5e7048 100%); }
  .chart { position: absolute; left: 0; top: 58px; width: 155px; height: 118px; background: linear-gradient(180deg, #ffffff, #eef5fb); }

  .flier-copy {
    position: absolute; left: 10px; right: 10px; top: 184px;
    font-size: 5.5px; line-height: 1.55; color: var(--ink);
  }
  .copy-rule { position: absolute; left: 10px; right: 10px; top: 222px; height: 1px; background: var(--line); }
  .thumbs { position: absolute; left: 10px; right: 10px; top: 230px; display: flex; gap: 4px; }
  .thumb { flex: 1; height: 30px; background: linear-gradient(180deg, #a9cbe6, #6f8a5c); }

  .flier-foot {
    position: absolute; left: 0; bottom: 0; width: 155px; height: 44px;
    background: linear-gradient(180deg, var(--paper) 0%, var(--sky) 100%);
    border-top: 2px solid var(--blue);
  }
  .brand {
    position: absolute; left: 10px; bottom: 14px;
    display: flex; align-items: center; gap: 4px; white-space: nowrap;
  }
  .brand-mark { width: 9px; height: 9px; background: var(--blue); flex: none; }
  .brand-name { font-size: 6.5px; font-weight: 700; color: var(--blue-dark); }

  .folder {
    position: absolute; left: 830px; top: 17px; width: 358px; height: 319px;
    background: radial-gradient(ellipse at 0% 30%, var(--paper-shade) 0%, var(--paper) 60%);
    border: 1px solid var(--line);
    box-shadow: 0 1px 4px rgba(0,0,0,.2); overflow: hidden;
  }
  .folder-brand {
    position: absolute; left: 118px; top: 92px;
    display: flex; align-items: center; gap: 8px; white-space: nowrap;
  }
  .folder-brand .brand-mark { width: 22px; height: 22px; }
  .folder-brand .brand-name { font-size: 15px; }
  .pocket { position: absolute; left: 0; bottom: 0; width: 358px; height: 112px; }
  .pocket-contact {
    position: absolute; left: 150px; bottom: 30px;
    font-size: 5.5px; line-height: 1.6; color: var(--paper); white-space: nowrap;
  }
  .pocket-dot {
    position: absolute; left: 128px; bottom: 33px;
    width: 14px; height: 14px; border-radius: 50%; background: var(--paper);
  }
</style>
</head>
<body>

<article class="flier" style="left:19px">
  <h2 class="flier-title">Initial Steps Overview</h2>
  <svg class="flier-wave" viewBox="0 0 155 46" aria-hidden="true">
    <path d="M0 10 C50 0 100 2 155 14 L155 46 L0 46 Z" fill="var(--blue)"/>
    <path d="M0 22 C60 8 110 12 155 26 L155 46 L0 46 Z" fill="var(--blue-light)"/>
  </svg>
  <div class="photo photo-house" role="img" aria-label="Two-storey family house with a front lawn"></div>
  <p class="flier-copy">We prepare each home with care so buyers can picture living there.</p>
  <div class="copy-rule"></div>
  <div class="thumbs">
    <div class="thumb" role="img" aria-label="Staged living room"></div>
    <div class="thumb" role="img" aria-label="Bright kitchen interior"></div>
    <div class="thumb" role="img" aria-label="House exterior at dusk"></div>
  </div>
  <div class="flier-foot"></div>
  <div class="brand"><span class="brand-mark"></span><span class="brand-name">Keystone Realty Group</span></div>
</article>

<article class="flier" style="left:180px">
  <h2 class="flier-title">Consumer Demand</h2>
  <svg class="flier-wave" viewBox="0 0 155 46" aria-hidden="true">
    <path d="M0 10 C50 0 100 2 155 14 L155 46 L0 46 Z" fill="var(--blue)"/>
    <path d="M0 22 C60 8 110 12 155 26 L155 46 L0 46 Z" fill="var(--blue-light)"/>
  </svg>
  <div class="photo photo-home" role="img" aria-label="Suburban home with a for-sale sign on the lawn"></div>
  <p class="flier-copy">Buyers expect listings that look ready, bright and inviting from day one.</p>
  <div class="flier-foot"></div>
  <div class="brand"><span class="brand-mark"></span><span class="brand-name">Keystone Realty Group</span></div>
</article>

<article class="flier" style="left:341px">
  <h2 class="flier-title">Service Style &amp; Pricing</h2>
  <svg class="flier-wave" viewBox="0 0 155 46" aria-hidden="true">
    <path d="M0 10 C50 0 100 2 155 14 L155 46 L0 46 Z" fill="var(--blue)"/>
    <path d="M0 22 C60 8 110 12 155 26 L155 46 L0 46 Z" fill="var(--blue-light)"/>
  </svg>
  <div class="photo photo-hands" role="img" aria-label="Business handshake closing a deal"></div>
  <p class="flier-copy">Clear packages and fair pricing let agents plan every listing with confidence.</p>
  <div class="flier-foot"></div>
  <div class="brand"><span class="brand-mark"></span><span class="brand-name">Keystone Realty Group</span></div>
</article>

<article class="flier" style="left:502px">
  <h2 class="flier-title">Value Consistency</h2>
  <svg class="flier-wave" viewBox="0 0 155 46" aria-hidden="true">
    <path d="M0 10 C50 0 100 2 155 14 L155 46 L0 46 Z" fill="var(--blue)"/>
    <path d="M0 22 C60 8 110 12 155 26 L155 46 L0 46 Z" fill="var(--blue-light)"/>
  </svg>
  <div class="photo photo-street" role="img" aria-label="Large family home on a tree-lined street"></div>
  <p class="flier-copy">Consistent presentation across every property builds trust with clients and buyers alike.</p>
  <div class="flier-foot"></div>
  <div class="brand"><span class="brand-mark"></span><span class="brand-name">Keystone Realty Group</span></div>
</article>

<article class="flier" style="left:663px">
  <h2 class="flier-title">Return on Investment</h2>
  <svg class="flier-wave" viewBox="0 0 155 46" aria-hidden="true">
    <path d="M0 10 C50 0 100 2 155 14 L155 46 L0 46 Z" fill="var(--blue)"/>
    <path d="M0 22 C60 8 110 12 155 26 L155 46 L0 46 Z" fill="var(--blue-light)"/>
  </svg>
  <svg class="chart" viewBox="0 0 155 118" role="img" aria-label="Bar chart of rising sale value">
    <line x1="20" y1="104" x2="140" y2="104" stroke="#9fb3c4" stroke-width="1"/>
    <rect x="28" y="82" width="16" height="22" fill="var(--blue-light)"/>
    <rect x="52" y="68" width="16" height="36" fill="var(--blue-light)"/>
    <rect x="76" y="52" width="16" height="52" fill="var(--blue)"/>
    <rect x="100" y="34" width="16" height="70" fill="var(--blue)"/>
    <rect x="124" y="18" width="16" height="86" fill="var(--blue-dark)"/>
    <polyline points="24,86 60,70 84,58 108,40 130,22" fill="none" stroke="#f2a23a" stroke-width="2"/>
    <polygon points="130,16 136,25 126,25" fill="#f2a23a"/>
  </svg>
  <p class="flier-copy">Staged homes often sell sooner and closer to asking price than others.</p>
  <div class="flier-foot"></div>
  <div class="brand"><span class="brand-mark"></span><span class="brand-name">Keystone Realty Group</span></div>
</article>

<section class="folder">
  <div class="folder-brand"><span class="brand-mark"></span><span class="brand-name">Keystone Realty Group</span></div>
  <svg class="pocket" viewBox="0 0 358 112" aria-hidden="true">
    <path d="M0 30 C120 0 240 6 358 24 L358 112 L0 112 Z" fill="var(--blue-light)"/>
    <path d="M0 42 C120 14 240 18 358 36 L358 112 L0 112 Z" fill="var(--blue)"/>
    <path d="M0 92 C120 80 240 84 358 96 L358 112 L0 112 Z" fill="var(--blue-dark)"/>
  </svg>
  <span class="pocket-dot"></span>
  <p class="pocket-contact">12 Harbor Lane, Portland OR<br>555 014 2290 · keystone-realty.example</p>
</section>

</body>
</html>
```